Pitch book for the 2025 K7R Global Stunt Cup event in Brenmoor, Kestrel County, USA

Title: Fueling the Future of Aeromodeling: Sponsor the 2025 K7R Global Stunt Cup
1. Event Overview
What: The 2025 IVO K7R Global Stunt Cup for Aerobatic Model Aircraft.
When: July 12–19, 2025.
Where: Guild of Miniature Aircraft Pilots (GMP) Headquarters, Brenmoor, Kestrel County.
Hosted by: Guild of Miniature Aircraft Pilots (GMP) in partnership with the Continental League of Remote Piloted Stunts (CLRPS).
Participants: Top pilots from across the globe, including juniors and female competitors.
2. Why Sponsor?
Shaping the Future Workforce: Inspire youth to explore careers in aerospace, aviation, and unmanned systems (drones, RPVs), bridging hobbies and high-tech industries like Veltrax, Corvane Dynamics, and more.
Brand Visibility: Engage with a global audience of enthusiasts, professionals, and media at a premier international event.
Community Impact: Support an event that promotes innovation, STEM education, and cultural exchange.
3. Key Features of the Event
Cutting-Edge Venue: Over 1,100 acres of flying space tailored for precision aerobatics.
Diverse Competitions: Featuring junior and female classifications alongside world-class competitors.
Global Audience: Media coverage, live streams, and on-site spectators.
4. Sponsorship Opportunities
Title Sponsor ($50,000):
Naming rights: "Your Brand Presents the 2025 K7R Global Stunt Cup."
Logo placement on all event materials, website, and livestreams.
Prime exhibit space at the venue.
Gold Sponsor ($25,000):
Prominent branding on materials and media.
Speaking opportunity at the opening or closing ceremony.
Silver Sponsor ($10,000):
Recognition in event communications.
Inclusion in the sponsor wall at the venue.
Event Sponsor ($5,000):
Branding on specific activities (e.g., banquet, practice days).
Custom Sponsorships: Tailored to fit corporate goals, including STEM outreach and branded giveaways.
5. Audience Demographics
Competitors: Over 100 elite pilots from 40+ countries.
Spectators & Supporters: Thousands of attendees, ranging from hobbyists to industry professionals.
Media Reach: Coverage by international aeromodelling and aerospace outlets.
6. STEM and Industry Connections
Showcase pathways from aeromodelling to careers in aviation, engineering, and defense.
Collaborate with sponsors on outreach programs for local schools and universities.
7. Marketing Benefits
Digital: Inclusion in newsletters, website, and social media campaigns.
On-Site Branding: Banners, booths, and branded giveaways.
Networking: Access to high-value attendees and industry leaders.
8. Budget Breakdown
Goal: Raise $180,000 to support the championship.
Funding Allocation:
$70,000: Event logistics (venue, staff, equipment).
$50,000: Participant support (travel subsidies, junior competitor outreach).
$30,000: Marketing and media coverage.
$20,000: Amenities and hospitality.
9. Call to Action
Be Part of the Legacy: Join us in creating a memorable event that not only crowns world champions but also inspires future innovators.
Contact Information:
Name: [Your Name]
Email: [Your Email]
Phone: [Your Phone]
Website: [Event Website Link]

```html
<!DOCTYPE html>
<html lang="en">
<head>
<meta charset="UTF-8">
<title>2025 K7R Global Stunt Cup – Sponsorship Trifold</title>
<link href="https://fonts.googleapis.com/css2?family=Montserrat:wght@600;700;800&family=Open+Sans:wght@400;600;700&display=swap" rel="stylesheet">
<style>
  :root{
    --blue:#1d5fbf;
    --navy:#123c7c;
    --sky:#4d95e0;
    --charcoal:#333538;
    --paper:#ffffff;
    --bg:#e9eaec;
    --ink:#2b2d31;
    --line:#e2e4e8;
    --rule:#d5dce8;
    --pale:#e8eef8;
    --muted:#c8ccd2;
    --tint:#cfe0f6;
  }
  *{box-sizing:border-box;margin:0;padding:0}
  html,body{width:900px;height:1200px;overflow:hidden;background:var(--bg)}
  body{font-family:"Open Sans",Arial,sans-serif;color:var(--ink);position:relative}
  .spread{position:absolute;left:60px;width:780px;height:560px;background:var(--paper);display:flex;box-shadow:0 4px 14px rgba(0,0,0,.18)}
  .spread--outside{top:30px}
  .spread--inside{top:620px}
  .panel{position:relative;width:260px;height:100%;overflow:hidden}
  .panel + .panel{border-left:1px solid var(--line)}
  .photo{position:absolute;left:0;width:100%}
  .photo--field{background:linear-gradient(160deg,#9cc3ea 0%,#c7d9ea 45%,#7d9a66 100%)}
  .photo--crowd{background:linear-gradient(150deg,#7aa7d6 0%,#d8c9a8 55%,#6f8a58 100%)}
  .photo--flag{background:linear-gradient(140deg,#2b4f8f 0%,#c23b3b 45%,#e9e4dc 70%,#5d7f4a 100%)}
  .photo--planes{background:linear-gradient(170deg,#b9d6f2 0%,#e7eef5 50%,#c44a3e 70%,#7a9960 100%)}
  .wave{position:absolute;left:0;width:100%;display:block}
  h1,h2,h3,.cover-title{font-family:"Montserrat",Arial,sans-serif}
  .heading{font-size:15px;font-weight:800;line-height:1.15;color:var(--blue)}
  .heading--light{color:var(--paper)}
  .heading--small{font-size:13px}
  .subheading{font-size:10px;font-weight:700;color:var(--navy);text-transform:uppercase;letter-spacing:.4px;margin:8px 0 3px}
  .body-text{font-size:8.2px;line-height:1.45;color:var(--ink)}
  .body-text--light{color:var(--pale)}
  .list{list-style:none}
  .list li{font-size:8px;line-height:1.4;padding-left:10px;position:relative;margin-bottom:2px}
  .list li::before{content:"";position:absolute;left:0;top:4px;width:5px;height:5px;background:var(--sky);border-radius:50%}
  .text-block{position:absolute;left:18px;right:18px}

  /* outside spread */
  .intro-band{position:absolute;top:0;left:0;width:100%;height:120px;background:var(--charcoal);padding:22px 18px}
  .intro-band .kicker{font-size:9px;color:var(--muted);letter-spacing:1px;text-transform:uppercase}
  .intro-band .heading{font-size:20px;margin-top:4px}
  .contact{position:absolute;left:18px;right:18px;top:350px}
  .contact-row{display:flex;align-items:center;gap:8px;margin-bottom:9px;font-size:9px;font-weight:600}
  .contact-icon{width:20px;height:20px;border-radius:50%;background:var(--blue);display:flex;align-items:center;justify-content:center;flex:none}
  .title-band{position:absolute;left:0;width:100%;background:var(--navy);color:var(--paper);padding:16px 18px}
  .title-band--blue{background:var(--blue)}
  .cover-title{font-size:26px;font-weight:800;line-height:1.05}
  .cover-sub{font-size:10px;font-weight:600;margin-top:6px;color:var(--tint)}
  .dates{font-size:9px;margin-top:6px;color:var(--pale)}

  /* inside spread */
  .callout{position:absolute;left:0;width:100%;background:var(--blue);color:var(--paper);padding:12px 18px}
  .callout--navy{background:var(--navy)}
  .callout h3{font-size:11px;font-weight:800;margin-bottom:4px}
  .tier{display:flex;justify-content:space-between;font-size:8px;border-bottom:1px solid var(--rule);padding:3px 0}
  .tier strong{color:var(--navy)}
  .budget-bar{height:8px;background:var(--sky);margin:2px 0 5px;border-radius:2px}
</style>
</head>
<body>

<section class="spread spread--outside">
  <article class="panel">
    <div class="intro-band">
      <p class="kicker">Supporting a</p>
      <h2 class="heading heading--light">Global Event</h2>
      <p class="body-text body-text--light" style="margin-top:6px">Join the sponsors helping bring the world's best aerobatic pilots to Brenmoor.</p>
    </div>
    <div class="photo photo--crowd" style="top:120px;height:200px" role="img" aria-label="Photo of competitors and supporters posing with model aircraft"></div>
    <svg class="wave" style="top:296px" width="260" height="30" viewBox="0 0 260 30" preserveAspectRatio="none"><path d="M0 12 Q70 0 140 14 T260 8 V30 H0Z" fill="#ffffff"/></svg>
    <div class="contact">
      <p class="subheading" style="margin:0 0 10px">Contact Information</p>
      <div class="contact-row"><span class="contact-icon"><svg width="10" height="10" viewBox="0 0 24 24"><path fill="#fff" d="M6.6 10.8a15 15 0 0 0 6.6 6.6l2.2-2.2a1 1 0 0 1 1-.25 11.4 11.4 0 0 0 3.6.57 1 1 0 0 1 1 1V20a1 1 0 0 1-1 1A17 17 0 0 1 3 4a1 1 0 0 1 1-1h3.5a1 1 0 0 1 1 1c0 1.25.2 2.45.57 3.57a1 1 0 0 1-.25 1z"/></svg></span>[Your Phone]</div>
      <div class="contact-row"><span class="contact-icon"><svg width="10" height="10" viewBox="0 0 24 24"><path fill="#fff" d="M2 5h20v14H2z M2 5l10 8 10-8" stroke="#1d5fbf" stroke-width="1.5"/></svg></span>[Your Email]</div>
      <div class="contact-row"><span class="contact-icon"><svg width="10" height="10" viewBox="0 0 24 24"><circle cx="12" cy="12" r="9" fill="none" stroke="#fff" stroke-width="2"/><path d="M3 12h18M12 3c3 3 3 15 0 18M12 3c-3 3-3 15 0 18" fill="none" stroke="#fff" stroke-width="1.5"/></svg></span>[Event Website Link]</div>
      <div class="contact-row"><span class="contact-icon"><svg width="10" height="10" viewBox="0 0 24 24"><path fill="#fff" d="M12 2a7 7 0 0 0-7 7c0 5 7 13 7 13s7-8 7-13a7 7 0 0 0-7-7zm0 9.5A2.5 2.5 0 1 1 12 6.5a2.5 2.5 0 0 1 0 5z"/></svg></span>GMP Headquarters, Brenmoor, Kestrel County</div>
    </div>
    <svg class="wave" style="bottom:0" width="260" height="60" viewBox="0 0 260 60" preserveAspectRatio="none"><path d="M0 30 Q80 5 160 28 T260 20 V60 H0Z" fill="#4d95e0"/><path d="M0 42 Q90 22 170 42 T260 36 V60 H0Z" fill="#123c7c"/></svg>
  </article>

  <article class="panel">
    <div class="photo photo--planes" style="top:0;height:230px" role="img" aria-label="Photo of aerobatic model aircraft lined up on the field"></div>
    <svg class="wave" style="top:200px" width="260" height="40" viewBox="0 0 260 40" preserveAspectRatio="none"><path d="M0 20 Q90 0 180 18 T260 10 V40 H0Z" fill="#123c7c"/></svg>
    <div class="title-band" style="top:238px;height:120px">
      <h2 class="cover-title" style="font-size:22px">2025 K7R</h2>
      <p class="cover-sub" style="font-size:12px;color:#fff">Global Stunt Cup</p>
      <p class="dates">July 12–19, 2025 · Brenmoor, Kestrel County</p>
    </div>
    <div class="photo photo--field" style="top:358px;height:202px" role="img" aria-label="Photo of pilots holding their model aircraft on the flying field"></div>
  </article>

  <article class="panel">
    <div class="photo photo--crowd" style="top:0;height:250px" role="img" aria-label="Photo of an international team with model aircraft"></div>
    <svg class="wave" style="top:222px" width="260" height="40" viewBox="0 0 260 40" preserveAspectRatio="none"><path d="M0 14 Q100 40 260 6 V40 H0Z" fill="#1d5fbf"/></svg>
    <div class="title-band title-band--blue" style="top:256px;height:140px">
      <h1 class="cover-title">2025 K7R</h1>
      <p class="cover-title" style="font-size:17px;margin-top:2px">Global Stunt Cup</p>
      <p class="cover-sub">&amp; Sponsorship Opportunities</p>
    </div>
    <div class="photo photo--field" style="top:396px;height:164px" role="img" aria-label="Photo of young pilots presenting their aircraft"></div>
  </article>
</section>

<section class="spread spread--inside">
  <article class="panel">
    <div class="text-block" style="top:18px">
      <h2 class="heading">Why We Need Your Support</h2>
      <p class="body-text" style="margin-top:6px">The IVO K7R Global Stunt Cup for Aerobatic Model Aircraft comes to GMP Headquarters, Brenmoor, Kestrel County, July 12–19, 2025. Hosted by the Guild of Miniature Aircraft Pilots (GMP) with the Continental League of Remote Piloted Stunts (CLRPS).</p>
    </div>
    <div class="photo photo--crowd" style="top:132px;height:140px" role="img" aria-label="Photo of competitors gathered at the event"></div>
    <div class="callout" style="top:272px;height:128px">
      <h3>Your donations will help us</h3>
      <p class="body-text body-text--light"><strong>Shape the future workforce:</strong> inspire youth toward aerospace, aviation and unmanned systems, bridging hobbies and industries like Veltrax and Corvane Dynamics.</p>
      <p class="body-text body-text--light" style="margin-top:3px"><strong>Community impact:</strong> innovation, STEM education and cultural exchange.</p>
    </div>
    <div class="text-block" style="top:408px">
      <p class="subheading" style="margin-top:0">Budget Breakdown · Goal $180,000</p>
      <p class="body-text">$70,000 Event logistics</p><div class="budget-bar" style="width:100%"></div>
      <p class="body-text">$50,000 Participant support</p><div class="budget-bar" style="width:71%"></div>
      <p class="body-text">$30,000 Marketing &amp; media</p><div class="budget-bar" style="width:43%"></div>
      <p class="body-text">$20,000 Amenities &amp; hospitality</p><div class="budget-bar" style="width:29%"></div>
    </div>
  </article>

  <article class="panel">
    <div class="photo photo--flag" style="top:0;height:170px" role="img" aria-label="Photo of pilots holding a national flag beside their aircraft"></div>
    <svg class="wave" style="top:146px" width="260" height="30" viewBox="0 0 260 30" preserveAspectRatio="none"><path d="M0 10 Q130 34 260 8 V30 H0Z" fill="#ffffff"/></svg>
    <div class="text-block" style="top:180px">
      <h2 class="heading heading--small">Sponsorship Opportunities</h2>
      <div style="margin-top:6px">
        <div class="tier"><strong>Title Sponsor</strong><span>$50,000</span></div>
        <div class="tier"><strong>Gold Sponsor</strong><span>$25,000</span></div>
        <div class="tier"><strong>Silver Sponsor</strong><span>$10,000</span></div>
        <div class="tier"><strong>Event Sponsor</strong><span>$5,000</span></div>
      </div>
      <p class="body-text" style="margin-top:5px">Title naming rights: "Your Brand Presents the 2025 K7R Global Stunt Cup." Custom sponsorships tailored to corporate goals, STEM outreach and branded giveaways.</p>
      <p class="subheading">Key Features of the Event</p>
      <ul class="list">
        <li>Over 1,100 acres of flying space for precision aerobatics</li>
        <li>Junior and female classifications alongside world-class pilots</li>
        <li>Media coverage, live streams and on-site spectators</li>
      </ul>
      <p class="subheading">Audience</p>
      <ul class="list">
        <li>Over 100 elite pilots from 40+ countries</li>
        <li>Thousands of hobbyists and industry professionals</li>
      </ul>
    </div>
    <svg class="wave" style="bottom:0" width="260" height="34" viewBox="0 0 260 34" preserveAspectRatio="none"><path d="M0 18 Q130 0 260 16 V34 H0Z" fill="#1d5fbf"/></svg>
  </article>

  <article class="panel">
    <div class="callout callout--navy" style="top:0;height:96px">
      <p class="body-text body-text--light" style="text-transform:uppercase;letter-spacing:.8px">Don't miss the chance</p>
      <h2 class="heading heading--light" style="margin-top:4px">Be Part of the Legacy</h2>
      <p class="body-text body-text--light" style="margin-top:4px">Help crown world champions and inspire future innovators.</p>
    </div>
    <div class="photo photo--planes" style="top:96px;height:170px" role="img" aria-label="Photo of pilots launching model aircraft at the competition"></div>
    <div class="text-block" style="top:278px">
      <h2 class="heading heading--small">Marketing Benefits</h2>
      <ul class="list" style="margin-top:5px">
        <li><strong>Digital:</strong> newsletters, website and social media campaigns</li>
        <li><strong>On-site branding:</strong> banners, booths and giveaways</li>
        <li><strong>Networking:</strong> high-value attendees and industry leaders</li>
      </ul>
      <p class="subheading">STEM &amp; Industry Connections</p>
      <p class="body-text">Showcase pathways from aeromodelling to careers in aviation, engineering and defense, and collaborate on outreach for local schools and universities.</p>
      <p class="subheading">Brand Visibility</p>
      <p class="body-text">Engage a global audience of enthusiasts, professionals and media at a premier international event.</p>
    </div>
    <svg class="wave" style="bottom:0" width="260" height="40" viewBox="0 0 260 40" preserveAspectRatio="none"><path d="M0 22 Q120 2 260 20 V40 H0Z" fill="#4d95e0"/><path d="M0 30 Q130 14 260 30 V40 H0Z" fill="#123c7c"/></svg>
  </article>
</section>

</body>
</html>
```